Retailer of Global Mobile Credit Web Redesign

We need a professional redesign (photoshop only - no coding) of an existing ecommerce website. Currently the website runs on Wordpress with woocommerce. We would like to keep that setup.
The attached draft shows a very crude mockup of ideas for the homepage. These are ideas only - we value your creative suggestions. I have also attached a preliminary logo, but this will likely be changed, so please don't base your color choices on it.
The draft also gives you the URL of the current site.
One of the sites which has a design we like it parcelwave.com.
The design is for ten pages - two of which are templates.
1. Homepage. Please see the attached draft for ideas. We like a darker picture with white lettering for the top of the page like Glintbarrow.com. The photo is just to give color, it is not meant to capture the user's attention but just be a background.
2. Countries page (/countries/). We need an elegant, easily navigable way to show the countries where we offer credit and the operators we offer for that country. If you feel that it is better to delete the countries page and instead show that information when you click "countries" in the menu, then please design how the menu would look.
3. How It Works (/how-it-works/)
4. My Account (/account-info/) prior to logging in or registering)
5. My Account (/account-info) after logging in
6. Privacy (/privacy/). A basic page with text.
7. Checkout (/checkout/). You won't have access to this page but I've attached a screenshot that shows you all the elements of the checkout page.
8. /how-to-sell-phone-credit/
9. /ghana/ Your design for this page will be used as a template for all the country pages e.g. /antigua/ and /el-salvador/
10. /product/recharge-velto-ghana/ Your design for this page will be used as a template for all operator pages e.g. /product/recharge-quorix-ghana/ or /product/recharge-bendi-costa-rica/
Thank you in advance for your submissions. Be sure to let us know if you have any questions.
Updates
Reason: Hello, I was on holiday. I like the design very much and look forward to finalizing it.
Industry/Entity Type
Telecommunications
Number of Pages Required
5+ page
Font styles to use
Look and feel
Each slider illustrates characteristics of the customer's brand and the style your logo design should communicate.

```html
<!DOCTYPE html>
<html lang="en">
<head>
<meta charset="utf-8">
<title>Topvane Credit Club – Mobile Credit</title>
<link href="https://fonts.googleapis.com/css2?family=Comfortaa:wght@300;400;700&family=Maven+Pro:wght@400;500;700&display=swap" rel="stylesheet">
<style>
:root{
  --blue:#1373bd;
  --orange:#f29b52;
  --band:#f4a05c;
  --white:#ffffff;
  --footer-bg:#f3f3f3;
  --footer-text:#555555;
  --ink:#333333;
}
*{margin:0;padding:0;box-sizing:border-box}
html,body{width:727px;height:1200px;overflow:hidden;background:var(--white)}
body{position:relative;font-family:"Maven Pro",sans-serif;color:var(--ink)}
.abs{position:absolute}
.site-header{left:0;top:0;width:727px;height:68px;background:var(--white)}
.brand{left:87px;top:24px;font-family:"Comfortaa",sans-serif;font-weight:700;font-size:15px;color:var(--blue);letter-spacing:.5px}
.menu-toggle{left:615px;top:28px;width:25px;height:20px}
.menu-toggle span{display:block;height:4px;background:var(--blue);margin-bottom:4px}
.hero{left:0;top:68px;width:727px;height:311px;background:linear-gradient(120deg,#5e6b3a 0%,#3f5228 40%,#6b7845 70%,#4a5a30 100%)}
.hero-title{left:88px;top:100px;font-family:"Comfortaa",sans-serif;font-weight:300;font-size:22px;line-height:26.5px;color:var(--white);letter-spacing:.8px}
.btn{display:flex;align-items:center;justify-content:center;background:var(--blue);color:var(--white);font-weight:500;letter-spacing:1px}
.hero-cta{left:87px;top:217px;width:209px;height:38px;font-size:14px}
.slider-dots{left:343px;top:291px;display:flex;gap:7px}
.slider-dots i{width:5px;height:5px;border-radius:50%;background:var(--white)}
.slider-dots i.active{background:var(--blue)}
.destination{left:0;top:379px;width:727px;height:51px;background:var(--band)}
.destination label{position:absolute;left:164px;top:17px;font-family:"Comfortaa",sans-serif;font-weight:700;font-size:13px;color:var(--white);letter-spacing:.8px}
.select{position:absolute;left:362px;top:13px;width:201px;height:25px;background:var(--white);font-size:9px;padding:9px 0 0 10px;color:#222}
.select svg{position:absolute;right:0;top:0}
.feature{top:486px;width:175px;height:214px;background:var(--blue);border-radius:3px;text-align:center;color:var(--white)}
.feature svg{margin-top:30px}
.feature h3{font-family:"Comfortaa",sans-serif;font-weight:700;font-size:15.5px;line-height:17.5px;color:var(--orange);letter-spacing:1px;margin-top:10px}
.feature p{font-size:11px;line-height:17.5px;letter-spacing:.5px;margin-top:11px}
.feature small{display:block;font-size:8px;font-weight:700;letter-spacing:.6px;margin-top:20px}
.how{left:0;top:746px;width:727px;height:312px;background:linear-gradient(180deg,#b8561a 0%,#e07a22 40%,#c35e1a 70%,#6a2f12 100%)}
.how h2{position:absolute;left:0;width:727px;top:44px;text-align:center;font-family:"Comfortaa",sans-serif;font-weight:700;font-size:15px;color:var(--white);letter-spacing:1.2px}
.step{top:100px;width:200px;text-align:center;color:var(--white)}
.step-num{width:25px;height:25px;border:2px solid var(--white);border-radius:50%;margin:0 auto;font-size:12px;font-weight:700;line-height:21px}
.step-label{font-family:"Comfortaa",sans-serif;font-weight:700;font-size:13px;line-height:17.5px;letter-spacing:.8px;margin-top:20px}
.how-cta{left:310px;top:251px;width:106px;height:30px;font-size:11.5px}
.site-footer{left:0;top:1058px;width:727px;height:142px;background:var(--footer-bg)}
.footer-col{top:36px;font-size:6.6px;line-height:11.5px;color:var(--footer-text);letter-spacing:.3px}
.copyright{left:88px;top:119px;font-size:6.6px;color:var(--footer-text)}
.social{left:567px;top:121px;display:flex;gap:5px}
.social i{width:5px;height:5px;border-radius:50%;background:#444}
</style>
</head>
<body>
<header class="site-header abs">
  <div class="brand abs">TOPVANE CREDIT CLUB</div>
  <div class="menu-toggle abs"><span></span><span></span><span></span></div>
</header>

<section class="hero abs" role="img" aria-label="Family enjoying a picnic on the grass, darkened background photo">
  <h1 class="hero-title abs">Purchase Mobile<br>Phone Credit<br>for yourself and<br>your family</h1>
  <a class="hero-cta btn abs">GET STARTED FOR FREE</a>
  <div class="slider-dots abs"><i class="active"></i><i></i><i></i><i></i></div>
</section>

<section class="destination abs">
  <label>Choose Your Destination</label>
  <div class="select">USA
    <svg width="30" height="25" viewBox="0 0 30 25"><line x1="1" y1="6" x2="1" y2="19" stroke="#ccc"/><polyline points="11,10 15,14 19,10" fill="none" stroke="#1373bd" stroke-width="2"/></svg>
  </div>
</section>

<article class="feature abs" style="left:87px">
  <svg width="26" height="38" viewBox="0 0 26 38"><rect x="2" y="2" width="22" height="34" rx="3" fill="none" stroke="#fff" stroke-width="2.5"/><line x1="2" y1="28" x2="24" y2="28" stroke="#fff" stroke-width="2"/><circle cx="13" cy="32" r="1.5" fill="#fff"/></svg>
  <h3>Instant<br>Recharge</h3>
  <p>Recharge Phones<br>worldwide instantly</p>
</article>
<article class="feature abs" style="left:276px">
  <svg width="40" height="40" viewBox="0 0 40 40" fill="none" stroke="#fff" stroke-width="1.6"><circle cx="20" cy="20" r="18"/><ellipse cx="20" cy="20" rx="8" ry="18"/><line x1="2" y1="20" x2="38" y2="20"/><line x1="20" y1="2" x2="20" y2="38"/><line x1="5" y1="11" x2="35" y2="11"/><line x1="5" y1="29" x2="35" y2="29"/></svg>
  <h3>Worldwide<br>Service</h3>
  <p>Coose from 50 operaters<br>in 30 countries</p>
</article>
<article class="feature abs" style="left:465px">
  <svg width="50" height="44" viewBox="0 0 50 44"><ellipse cx="26" cy="22" rx="20" ry="15" fill="#fff"/><rect x="13" y="30" width="7" height="11" rx="2" fill="#fff"/><rect x="30" y="30" width="7" height="11" rx="2" fill="#fff"/><circle cx="6" cy="20" r="5" fill="#fff"/><rect x="20" y="7" width="10" height="2" fill="#1373bd"/></svg>
  <h3>Transparent<br>Prices</h3>
  <p>See the price and<br>recharge amount</p>
  <small>No hidden Fees</small>
</article>

<section class="how abs" role="img" aria-label="Family silhouette playing on a beach at sunset">
  <h2>How It Works</h2>
  <div class="step abs" style="left:74px"><div class="step-num">1</div><div class="step-label">Join For Free</div></div>
  <div class="step abs" style="left:264px"><div class="step-num">2</div><div class="step-label">Choose Your<br>Recharge</div></div>
  <div class="step abs" style="left:452px"><div class="step-num">3</div><div class="step-label">Pay Securely With<br>Your Card via paywisp</div></div>
  <svg class="abs" style="left:232px;top:196px" width="110" height="30" viewBox="0 0 110 30" fill="none" stroke="#fff" stroke-width="2"><path d="M2 18 Q45 30 102 6"/><polyline points="90,5 102,6 97,17"/></svg>
  <svg class="abs" style="left:422px;top:196px" width="110" height="30" viewBox="0 0 110 30" fill="none" stroke="#fff" stroke-width="2"><path d="M2 18 Q45 30 102 6"/><polyline points="90,5 102,6 97,17"/></svg>
  <a class="how-cta btn abs">LEARN MORE</a>
</section>

<footer class="site-footer abs">
  <div class="footer-col abs" style="left:87px">Home<br>Countries<br>How It Works<br>My Account/Join for Free</div>
  <div class="footer-col abs" style="left:215px">FAQ<br>Contact us<br>Partners &amp; Affiliates</div>
  <div class="footer-col abs" style="left:355px">Terms and conditions<br>Privacy policy<br>Cookies policy<br>Sitemap</div>
  <div class="footer-col abs" style="left:497px">Calverin LLC, a Massachusetts (USA)<br>limited liability company<br>48 Linden Hollow Rd, Ashford, MA 01990<br>ops@calverin.com</div>
  <div class="copyright abs">© 2016 Company Name | All Rights Reserved</div>
  <div class="social abs"><i></i><i></i><i></i><i></i><i></i><i></i><i></i></div>
</footer>
</body>
</html>
```